Fine Art business needs new website

We need a simple website with a home page, about us page, New sculptures, Sold sculptures, and a contact us page.Our sculptures are very high end one of a kind pieces. As such we need the site to be VERY elegant and professional. Lastly, because I'll be updating pictures on the website on a monthly basis it needs to be user friendly to update (Wordpress is preferred). The only branding we have so far for the business is a business card.
Updates
I wasn't completely ready when this project launched, also I am on the road right now and haven't been able to be as responsive to all you designers as I would like. I will work on giving feedback to all the top designs we've received so far. Thank you all so much for your participation and hardwork.
Target Market(s)
High end customers (affluent), art collectors, interior decorators/designers
Industry/Entity Type
Art Gallery
Coding
Coded - Design and coding required
Number of Pages Required
5+ page
Requirements
Must have
- Easily editable picture gallery for myself so that I can add new pieces(pictures of the pieces), remove sold pieces, etc. I would like the website to be built in wordpress so I can update it. I currently use sitekeeperpro through Netbirch for my other business website and would like to do the same for this one.
- Pages:
- -Intro page with featured pieces
- -Current pieces gallery (for sale) mainly a picture gallery
- -Sculptures archive (sold pieces) another picture gallery
- -About us: Pull-down of -about the artist (attached content)
- -Artistic Process (attached content)
- -Show Schedule:
- -one page dedicated to "friends of QMW" (basically a link page)
- TO BE CLEAR "www.lanternhollow.com" IS A TOTALLY DIFFERENT SITE AND I'M NOT TRYING TO COMBINE THE TWO OR JOIN THEM INTO ONE. This page needs be more elegant and seperate from the Lantern Hollow site.
- UPDATE: I'd like a link to the QMW Facebook page: https://www.facebook.com/quillmarkworks/
Nice to have
- I would like the pictures on the gallery pages able to have text connected with them (Materials, price)
- I would like the site style and fonts to be similar to our business cards we've already had designed (picture attached).
Should not have
- Too much flash or other things that will make the site slow to load.

```html
<!DOCTYPE html>
<html lang="en">
<head>
<meta charset="utf-8">
<title>Quillmark Works – Fine Art Sculptures</title>
<link href="https://fonts.googleapis.com/css2?family=Cormorant+Garamond:wght@400;500;600&family=Open+Sans:wght@400;600;700&display=swap" rel="stylesheet">
<style>
:root{
  --purple:#6a3f9e;
  --purple-dark:#4b2b78;
  --purple-light:#9265c6;
  --ink:#222028;
  --text:#5d5a63;
  --muted:#9a97a0;
  --dark:#1d1a22;
  --dark-2:#2b2633;
  --line:#e4e1e8;
  --paper:#f4f3f6;
  --white:#ffffff;
  --serif:"Cormorant Garamond", Georgia, serif;
  --sans:"Open Sans", Arial, sans-serif;
}
*{box-sizing:border-box;margin:0;padding:0}
html,body{width:1200px;height:4639px;overflow:hidden}
body{font-family:var(--sans);color:var(--text);background:var(--white);position:relative}
.abs{position:absolute}
.btn{display:inline-block;font:700 11px/1 var(--sans);letter-spacing:1px;text-transform:uppercase;padding:11px 20px;color:var(--white);background:var(--purple);text-decoration:none}
.btn--dark{background:var(--ink)}
.btn--outline{background:var(--white);color:var(--ink);border:1px solid var(--line);box-shadow:0 2px 6px rgba(0,0,0,.08)}
.section-label{font:600 10px var(--sans);color:var(--purple);letter-spacing:2px;text-transform:uppercase}
.section-title{font:500 32px/1 var(--serif);color:var(--ink);text-transform:uppercase;letter-spacing:1px}
.section-title::after{content:"";display:block;width:70px;height:3px;background:var(--purple);margin-top:10px}
.section-title--center{text-align:center}
.section-title--center::after{margin:10px auto 0}
.section-title--light{color:var(--white)}
.section-title--light::after{background:var(--white)}
.photo{display:block}

/* header */
.topbar{left:0;top:0;width:1200px;height:24px;background:linear-gradient(90deg,var(--purple-dark),var(--purple-light));}
.topbar__info{right:180px;top:5px;color:var(--white);font:600 11px var(--sans);display:flex;gap:26px}
.topbar__info span{display:flex;align-items:center;gap:6px}
.nav-bar{left:0;top:24px;width:1200px;height:70px;background:var(--white);box-shadow:0 2px 6px rgba(0,0,0,.06);z-index:2}
.brand{left:172px;top:20px;display:flex;align-items:center;gap:10px;font:600 17px var(--serif);letter-spacing:2px;color:var(--ink)}
.brand__mark{width:14px;height:14px;border-radius:50%;background:var(--purple)}
.nav{left:405px;top:30px;display:flex;gap:30px;list-style:none}
.nav a{font:500 14px var(--serif);color:var(--ink);text-decoration:none;text-transform:uppercase;letter-spacing:.5px;padding-bottom:6px}
.nav a.is-active{color:var(--purple);border-bottom:2px solid var(--purple)}

/* hero */
.hero{left:0;top:94px;width:1200px;height:581px;background:linear-gradient(100deg,#5a3b22 0%,#b47b43 30%,#e2b17a 55%,#c08a54 75%,#6f4a2c 100%)}
.hero__shade{left:0;top:0;width:1200px;height:581px;background:linear-gradient(90deg,rgba(0,0,0,0) 45%,rgba(40,25,15,.45) 100%)}
.hero__text{left:790px;top:255px;color:var(--white)}
.hero__kicker{font:500 20px var(--serif);letter-spacing:4px}
.hero__title{font:500 54px/1 var(--serif);letter-spacing:3px;margin-top:4px}
.hero__sub{font:600 11px var(--sans);letter-spacing:4px;margin-top:10px}
.hero .btn{margin-top:26px}

/* welcome */
.welcome-photo{left:0;top:675px;width:420px;height:345px;background:linear-gradient(135deg,#eeeae6,#bfb3a3 55%,#8c7c6a)}
.welcome{left:442px;top:722px;width:720px}
.welcome p{font:400 12.5px/2 var(--sans);margin-top:26px}
.welcome .btn{margin-top:20px}

/* galleries */
.gallery-bg{left:0;top:1020px;width:1200px;height:1192px;background:linear-gradient(180deg,#ffffff,var(--paper) 40%,#f1eff5 70%,#ffffff)}
.gallery-head{left:186px;width:804px;display:flex;justify-content:space-between;align-items:flex-end}
.arrow{width:34px;height:34px;display:flex;align-items:center;justify-content:center}
.cards{left:186px;display:flex;gap:31px}
.card{width:247px;background:var(--white);box-shadow:0 2px 10px rgba(0,0,0,.08)}
.card__photo{height:303px;position:relative;background:radial-gradient(circle at 50% 45%,#7a6a5a,#1f1c1c 70%)}
.card__photo--b{background:radial-gradient(circle at 50% 45%,#5a4a6a,#1c1a1f 70%)}
.card__photo--c{background:radial-gradient(circle at 50% 45%,#8a8f9a,#1c1c1f 70%)}
.card__photo--d{background:radial-gradient(circle at 50% 45%,#2f6a4a,#1c1f1c 70%)}
.card__photo--e{background:radial-gradient(circle at 50% 45%,#a57a3a,#1f1c18 70%)}
.card__body{padding:16px 18px 16px}
.card__title{font:500 13px/1.35 var(--serif);color:var(--ink);text-transform:uppercase}
.card__price{font:600 12px var(--sans);color:var(--ink);margin-top:8px}
.card__buy{display:inline-block;font:700 10px var(--sans);color:var(--ink);letter-spacing:.5px;margin-top:8px;padding:5px 8px}
.card__buy.is-hover{background:var(--purple);color:var(--white)}
.sold-tag{position:absolute;right:0;bottom:0;background:var(--purple);color:var(--white);font:600 10px var(--sans);padding:8px 12px;letter-spacing:.5px}

/* artist */
.artist{left:0;top:2212px;width:1200px;height:541px;background:linear-gradient(135deg,#7b50b3,#5b3593 55%,#4a2a7d)}
.artist__intro{left:220px;top:110px;width:760px;text-align:center;color:rgba(255,255,255,.85);font:400 12px/1.9 var(--sans)}
.artist__photo{left:186px;top:185px;width:300px;height:303px;background:linear-gradient(160deg,#c7b49a,#7b6450 60%,#3e3230)}
.artist__name{left:504px;top:200px;color:var(--white);font:500 20px var(--serif);letter-spacing:2px}
.artist__bio{left:504px;top:232px;width:485px;color:rgba(255,255,255,.85);font:400 12px/1.85 var(--sans)}
.team{left:504px;top:355px;display:flex;gap:28px}
.team__item{width:140px;text-align:center}
.team__photo{height:93px;background:linear-gradient(150deg,#bfa98c,#6a5646)}
.team__name{color:var(--white);font:700 11px var(--sans);letter-spacing:.5px;margin-top:12px;text-transform:uppercase}

/* video + blog */
.dark-band{left:0;top:3170px;width:1200px;height:604px;background:linear-gradient(180deg,#2d2736,var(--dark) 60%,#241f2b)}
.video{left:186px;top:2883px;width:798px;height:371px;border:5px solid var(--white);box-shadow:0 6px 20px rgba(0,0,0,.25);background:linear-gradient(180deg,#3a3a3f,#141416 80%);display:flex;align-items:center;justify-content:center}
.play{width:54px;height:54px;border-radius:50%;background:var(--purple);display:flex;align-items:center;justify-content:center}
.blog{left:186px;top:3381px;display:flex;gap:31px}
.post{width:247px;height:318px;background:var(--white);position:relative}
.post__photo{height:170px;position:relative;background:linear-gradient(150deg,#6d7b8a,#2c3440)}
.post__photo--b{background:linear-gradient(150deg,#d7cfc3,#8d7c68)}
.post__photo--c{background:linear-gradient(150deg,#c9cbd0,#5d6168)}
.post__date{position:absolute;right:10px;top:0;width:34px;height:44px;background:var(--purple);color:var(--white);text-align:center;font:700 14px/1 var(--sans);padding-top:7px}
.post__date small{display:block;font:600 8px var(--sans);margin-top:3px}
.post__body{padding:16px 18px;text-align:center}
.post__title{font:500 17px/1.2 var(--serif);color:var(--ink)}
.post__text{font:400 11px/1.6 var(--sans);margin-top:8px}
.post__corner{position:absolute;right:0;bottom:0;width:0;height:0;border-left:26px solid transparent;border-bottom:26px solid var(--purple)}

/* testimonials */
.testimonial{width:294px;height:170px;background:var(--white);box-shadow:0 4px 16px rgba(0,0,0,.08);padding:22px 24px}
.testimonial--faded{box-shadow:none;opacity:.35}
.testimonial__text{font:400 11px/1.7 var(--sans)}
.person{display:flex;align-items:center;gap:10px;margin-top:14px}
.person__avatar{width:34px;height:34px;border-radius:50%;background:#c9c3cf}
.person__name{font:700 11px var(--sans);color:var(--ink)}
.person__role{font:400 10px var(--sans);color:var(--muted)}
.dots{display:flex;gap:8px}
.dots span{width:16px;height:16px;border-radius:50%;background:var(--purple)}

/* cta + footer */
.footer{left:0;top:4268px;width:1200px;height:325px;background:linear-gradient(180deg,#221e27,#16131a)}
.cta{left:176px;top:4231px;width:820px;height:84px;background:linear-gradient(90deg,var(--purple-dark),var(--purple) 60%,var(--purple-light));display:flex;align-items:center;padding:0 22px;z-index:2}
.cta__brand{display:flex;align-items:center;gap:8px;color:var(--white);font:600 18px var(--serif);width:200px}
.cta__brand i{width:12px;height:12px;background:var(--white);display:block}
.cta__text{color:var(--white);font:500 18px/1.25 var(--serif);letter-spacing:1px;flex:1}
.cta .btn{background:var(--dark);padding:12px 26px}
.foot-col{top:4360px}
.foot-col h4{color:var(--white);font:700 12px var(--sans);letter-spacing:1px;text-transform:uppercase;margin-bottom:20px}
.foot-links{list-style:none}
.foot-links li{color:#c8c4cc;font:400 11px/2.1 var(--sans)}
.foot-links li::before{content:"›";color:var(--purple-light);margin-right:7px}
.contact-line{display:flex;gap:10px;color:#c8c4cc;font:400 11px/1.5 var(--sans);margin-bottom:14px}
.contact-icon{width:22px;height:22px;border-radius:50%;background:var(--purple);flex:none;display:flex;align-items:center;justify-content:center}
.map{width:232px;height:124px;background:linear-gradient(135deg,#e8e6e1,#d7dde0)}
.field{width:210px;height:24px;background:var(--white);font:400 10px/24px var(--sans);color:var(--muted);padding-left:8px;margin-bottom:8px}
.field--tall{height:44px}
.bottombar{left:0;top:4593px;width:1200px;height:46px;background:linear-gradient(90deg,var(--purple-dark),var(--purple) 70%,var(--purple-light));display:flex;justify-content:space-between;align-items:center;padding:0 176px}
.bottombar p{color:var(--white);font:400 10px var(--sans);letter-spacing:.5px}
.social{display:flex;align-items:center;gap:8px;color:var(--white);font:700 10px var(--sans)}
.social span{width:18px;height:18px;border-radius:50%;background:var(--white)}
</style>
</head>
<body>

<!-- Header -->
<div class="abs topbar">
  <div class="abs topbar__info">
    <span><svg width="10" height="10" viewBox="0 0 24 24"><path fill="#fff" d="M6.6 10.8a15 15 0 006.6 6.6l2.2-2.2a1 1 0 011-.25 11.4 11.4 0 003.6.6 1 1 0 011 1V20a1 1 0 01-1 1A17 17 0 013 4a1 1 0 011-1h3.5a1 1 0 011 1c0 1.25.2 2.45.6 3.6a1 1 0 01-.25 1z"/></svg>(555) 014-2290</span>
    <span><svg width="11" height="9" viewBox="0 0 24 18"><path fill="none" stroke="#fff" stroke-width="2" d="M1 1h22v16H1zM1 1l11 9 11-9"/></svg>INFO@QUILLMARKWORKS.COM</span>
  </div>
</div>
<header class="abs nav-bar">
  <div class="abs brand"><span class="brand__mark"></span>QUILLMARK WORKS</div>
  <ul class="abs nav">
    <li><a class="is-active" href="#">Home</a></li>
    <li><a href="#">About Us</a></li>
    <li><a href="#">New Sculptures</a></li>
    <li><a href="#">Sold Sculptures</a></li>
    <li><a href="#">Events</a></li>
    <li><a href="#">Contact Us</a></li>
  </ul>
</header>

<!-- Hero -->
<section class="abs hero" role="img" aria-label="Gallery interior with framed paintings on the walls and sculptures on white plinths">
  <div class="abs hero__shade"></div>
  <div class="abs hero__text">
    <div class="hero__kicker">QUARTZ</div>
    <div class="hero__title">AMETHYST</div>
    <div class="hero__sub">HIGH QUALITY SCULPTURES</div>
    <a class="btn" href="#">Buy Now</a>
  </div>
</section>

<!-- Welcome -->
<div class="abs welcome-photo photo" role="img" aria-label="Burlap gift pouches with business cards"></div>
<section class="abs welcome">
  <h2 class="section-title">Welcome to Quillmark Works</h2>
  <p>Lantern Hollow, known to some as the "Ember Stone Guys", began more than twenty years ago when its founder first cut open a rough stone and found a glittering crystal cave inside. That moment grew into a lifelong craft of shaping quartz, amethyst and agate into refined one of a kind sculptures. Each piece is cleaned, cut and polished by hand, then mounted on a custom base so that collectors can enjoy the natural beauty of the stone for generations to come.</p>
  <a class="btn btn--dark" href="#">Read More</a>
</section>

<!-- Galleries -->
<div class="abs gallery-bg"></div>

<div class="abs gallery-head" style="top:1058px">
  <div><div class="section-label">The Latest</div><h2 class="section-title" style="margin-top:6px">New Sculptures</h2></div>
  <a class="btn btn--outline" href="#">View All</a>
</div>
<div class="abs arrow" style="left:120px;top:1298px"><svg width="14" height="24" viewBox="0 0 14 24"><path d="M12 2L2 12l10 10" fill="none" stroke="#cfcbd4" stroke-width="2"/></svg></div>
<div class="abs arrow" style="left:1050px;top:1298px"><svg width="14" height="24" viewBox="0 0 14 24"><path d="M2 2l10 10-10 10" fill="none" stroke="#cfcbd4" stroke-width="2"/></svg></div>
<div class="abs cards" style="top:1166px">
  <article class="card">
    <div class="card__photo" role="img" aria-label="Amethyst cathedral sculpture on a black background"></div>
    <div class="card__body"><h3 class="card__title">Amethyst Cathedral - Unique #29 - 17" Tall</h3><div class="card__price">$20.00</div><a class="card__buy" href="#">BUY NOW</a></div>
  </article>
  <article class="card">
    <div class="card__photo card__photo--b" role="img" aria-label="Dark crystal sculpture on a black background"></div>
    <div class="card__body"><h3 class="card__title">Amethyst Cathedral - And Unique #29 - 17" Tall</h3><div class="card__price">$20.00</div><a class="card__buy is-hover" href="#">BUY NOW</a></div>
  </article>
  <article class="card">
    <div class="card__photo card__photo--c" role="img" aria-label="Agate slice sculpture on a black background"></div>
    <div class="card__body"><h3 class="card__title">Amethyst Cathedral - And Unique #29 - 17" Tall</h3><div class="card__price">$50.00</div><a class="card__buy" href="#">BUY NOW</a></div>
  </article>
</div>

<div class="abs gallery-head" style="top:1676px">
  <div><div class="section-label">The Archive</div><h2 class="section-title" style="margin-top:6px">Sold Sculptures</h2></div>
  <a class="btn" href="#">View All</a>
</div>
<div class="abs cards" style="top:1778px">
  <article class="card">
    <div class="card__photo card__photo--c" role="img" aria-label="Pale quartz sculpture on a black background"><span class="sold-tag">SOLD FOR $20.00</span></div>
    <div class="card__body"><h3 class="card__title">Amethyst Cathedral - Unique #29 - 17" Tall</h3></div>
  </article>
  <article class="card">
    <div class="card__photo card__photo--d" role="img" aria-label="Green mineral sculpture on a black background"><span class="sold-tag">SOLD FOR $20.00</span></div>
    <div class="card__body"><h3 class="card__title">Amethyst Cathedral - And Unique #29 - 17" Tall</h3></div>
  </article>
  <article class="card">
    <div class="card__photo card__photo--e" role="img" aria-label="Golden polished stone sculpture on a black background"><span class="sold-tag">SOLD FOR $50.00</span></div>
    <div class="card__body"><h3 class="card__title">Amethyst Cathedral - And Unique #29 - 17" Tall</h3></div>
  </article>
</div>

<!-- Artist -->
<section class="abs artist">
  <h2 class="abs section-title section-title--center section-title--light" style="left:0;top:48px;width:1200px">Meet Our Artist</h2>
  <p class="abs artist__intro">Every sculpture begins with a stone chosen by hand in the field, studied for its colour and structure, then cut and finished in the studio. Meet the people who give each piece its final form and character.</p>
  <div class="abs artist__photo photo" role="img" aria-label="The artist standing in the workshop wearing a leather apron"></div>
  <h3 class="abs artist__name">MARLOW FINCH</h3>
  <p class="abs artist__bio">Being the son of a local rock gem enthusiast, Marlow grew up among stones and minerals. Through years of travel to shows and fairs across the West, he learned to read each rock and see the sculpture hidden within it. What started as a passion has become a full time craft, and he now shares that love for natural beauty with collectors everywhere.</p>
  <div class="abs team">
    <div class="team__item"><div class="team__photo photo" role="img" aria-label="Team member in the workshop"></div><div class="team__name">Edwin Hale</div></div>
    <div class="team__item"><div class="team__photo photo" role="img" aria-label="Team member at a show booth"></div><div class="team__name">Tobias Reyes</div></div>
    <div class="team__item"><div class="team__photo photo" role="img" aria-label="Team member cutting stone"></div><div class="team__name">Owen Finch</div></div>
  </div>
</section>

<!-- Video -->
<h2 class="abs section-title section-title--center" style="left:0;top:2805px;width:1200px">Our Video</h2>
<div class="abs dark-band"></div>
<div class="abs video" role="img" aria-label="Video still of sculptures displayed in a dark showroom">
  <div class="play"><svg width="18" height="20" viewBox="0 0 18 20"><path d="M2 1l15 9-15 9z" fill="#fff"/></svg></div>
</div>

<!-- Blog -->
<h2 class="abs section-title section-title--center section-title--light" style="left:0;top:3310px;width:1200px">Latest Blog</h2>
<div class="abs blog">
  <article class="post">
    <div class="post__photo photo" role="img" aria-label="Large polished stone sphere"><div class="post__date">12<small>OCT</small></div></div>
    <div class="post__body"><h3 class="post__title">Ut wisi enim ad minim veniam, quis nostrud exerci tation</h3><p class="post__text">Notes from the studio on cutting and polishing a new sphere for the fall collection.</p></div>
    <span class="post__corner"></span>
  </article>
  <article class="post">
    <div class="post__photo post__photo--b photo" role="img" aria-label="Gift pouches and cards on a table"><div class="post__date">22<small>OCT</small></div></div>
    <div class="post__body"><h3 class="post__title">Ut wisi enim ad minim veniam, quis nostrud exerci tation</h3><p class="post__text">A look at how each finished piece is packed and prepared for its new home.</p></div>
    <span class="post__corner"></span>
  </article>
  <article class="post">
    <div class="post__photo post__photo--c photo" role="img" aria-label="White show tent at an outdoor art fair"><div class="post__date">22<small>OCT</small></div></div>
    <div class="post__body"><h3 class="post__title">Ut wisi enim ad minim veniam, quis nostrud exerci tation</h3><p class="post__text">Our show schedule for the season and where you can see the collection in person.</p></div>
    <span class="post__corner"></span>
  </article>
</div>
<a class="abs btn" href="#" style="left:555px;top:3752px">View All</a>

<!-- Testimonials -->
<div class="abs section-label" style="left:272px;top:3850px">What They Say</div>
<h2 class="abs section-title" style="left:272px;top:3870px">Customer Testimonials</h2>
<div class="abs testimonial" style="left:294px;top:3944px">
  <p class="testimonial__text">"The amethyst piece we bought is the centre of our living room. Every guest asks about it, and the quality is beyond what we hoped for. Truly a work of art."</p>
  <div class="person"><span class="person__avatar"></span><div><div class="person__name">Jared Voss</div><div class="person__role">Art Collector</div></div></div>
</div>
<div class="abs testimonial testimonial--faded" style="left:634px;top:3944px">
  <p class="testimonial__text">"Beautiful craftsmanship and a pleasure to work with. The sculpture arrived safely and looks even better than the photos did."</p>
  <div class="person"><span class="person__avatar"></span><div><div class="person__name">Nora Lind</div><div class="person__role">Interior Designer</div></div></div>
</div>
<div class="abs testimonial testimonial--faded" style="left:930px;top:3944px">
  <p class="testimonial__text">"A stunning one of a kind piece. We will certainly return to add more to our home collection."</p>
  <div class="person"><span class="person__avatar"></span><div><div class="person__name">Ella Park</div><div class="person__role">Collector</div></div></div>
</div>
<div class="abs dots" style="left:294px;top:4152px"><span></span><span></span></div>

<!-- Footer -->
<footer class="abs footer"></footer>
<div class="abs cta">
  <div class="cta__brand"><i></i>Lantern Hollow</div>
  <div class="cta__text">LOOKING FOR MORE STONE ART<br>VISIT SITE LANTERN HOLLOW</div>
  <a class="btn" href="#">Visit Site</a>
</div>

<div class="abs foot-col" style="left:176px">
  <h4>Quick Links</h4>
  <ul class="foot-links"><li>Home</li><li>About Us</li><li>New Sculptures</li><li>Sold Sculptures</li><li>Events</li><li>Contact Us</li></ul>
</div>
<div class="abs foot-col" style="left:331px;width:190px">
  <h4>Contact Info</h4>
  <div class="contact-line"><span class="contact-icon"><svg width="10" height="12" viewBox="0 0 20 24"><path fill="#fff" d="M10 0a8 8 0 018 8c0 6-8 16-8 16S2 14 2 8a8 8 0 018-8zm0 5a3 3 0 100 6 3 3 0 000-6z"/></svg></span><span>PO Box 4410<br>Alder Ridge CO<br>80000</span></div>
  <div class="contact-line"><span class="contact-icon"><svg width="10" height="10" viewBox="0 0 24 24"><path fill="#fff" d="M6.6 10.8a15 15 0 006.6 6.6l2.2-2.2a1 1 0 011-.25 11.4 11.4 0 003.6.6 1 1 0 011 1V20a1 1 0 01-1 1A17 17 0 013 4a1 1 0 011-1h3.5a1 1 0 011 1c0 1.25.2 2.45.6 3.6a1 1 0 01-.25 1z"/></svg></span><span>+1 (555) 014-2290</span></div>
  <div class="contact-line"><span class="contact-icon"><svg width="11" height="9" viewBox="0 0 24 18"><path fill="none" stroke="#fff" stroke-width="2" d="M1 1h22v16H1zM1 1l11 9 11-9"/></svg></span><span>info@quillmarkworks.com</span></div>
</div>
<div class="abs foot-col" style="left:541px">
  <h4>Find Us On Map</h4>
  <div class="map" role="img" aria-label="Street map showing the studio location"></div>
</div>
<div class="abs foot-col" style="left:810px">
  <h4>Quick Contact</h4>
  <div class="field">Name</div>
  <div class="field">Email</div>
  <div class="field field--tall">Message</div>
  <a class="btn" href="#" style="padding:9px 16px">Submit Info</a>
</div>

<div class="abs bottombar">
  <p>© COPYRIGHT QUILLMARK WORKS. ALL RIGHTS RESERVED</p>
  <div class="social">FOLLOW US <span aria-label="Social link"></span><span aria-label="Social link"></span><span aria-label="Social link"></span><span aria-label="Social link"></span><span aria-label="Social link"></span></div>
</div>

</body>
</html>
```